New Business Card Design Project

Make a kick ass business card for The Otter Tea Mug, using the designs. I also might like the 2nd place design logo on the back? Maybe all black with that? Not sure. Also, I'm cool with it being on metal, plastic, glass? or whatever for the business card. Maybe shaped like a shark? Let me know what else you need? Would like designs in the next day or so. Thank you.
Target Market(s)
Anyone that is cool
Contact Information for Business Card
Name: Dorian Fenwick
Phone: 317.594.8126
inventor/creator/entrepreneur/owner
www.theottertyeamug.example
social media links
https://www.facebook.com/theottertyeamug
https://twitter.com/otter_brew
https://www.instagram.com/theottertyeamug/
I'll get the Pinterest one soon
Colors
Designer to choose colors to be used in the design.
Requirements
Must have
- The Otter Tea Mug
- www.theottertyeamug.example
- social media tags?
- My logos and picture/photo of wine glass
Nice to have
- Maybe shaped like a wine glass or shark
- I'll let you decide but my same colors from my website would be nice

```html
<!DOCTYPE html>
<html lang="en">
<head>
<meta charset="utf-8">
<title>The Otter Tea Mug – Business Card</title>
<link rel="stylesheet" href="https://fonts.googleapis.com/css2?family=Montserrat:wght@300;400&family=Yellowtail&display=swap">
<style>
  :root {
    --card-bg: #2e1213;
    --text-light: #d6d4d4;
    --text-soft: #b9aeae;
    --accent-red: #e3163f;
  }
  html, body {
    margin: 0;
    padding: 0;
    width: 1200px;
    height: 777px;
    overflow: hidden;
    background: var(--card-bg);
  }
  .card {
    position: relative;
    width: 1200px;
    height: 777px;
    background: var(--card-bg);
    overflow: hidden;
  }
  .berry-wave {
    position: absolute;
    left: 0;
    top: 0;
    width: 1200px;
    height: 777px;
  }
  .brand-mark {
    position: absolute;
    left: 385px;
    top: 205px;
    width: 430px;
    margin: 0;
    text-align: center;
    font-family: "Montserrat", sans-serif;
    font-weight: 300;
    font-size: 40px;
    line-height: 1;
    color: var(--text-light);
  }
  .glass-art {
    position: absolute;
    left: 1040px;
    top: 66px;
    width: 77px;
    height: 167px;
  }
  .wordmark {
    position: absolute;
    left: 0;
    top: 360px;
    width: 1200px;
    margin: 0;
    text-align: center;
    font-family: "Montserrat", sans-serif;
    font-weight: 300;
    font-size: 104px;
    letter-spacing: 1px;
    line-height: 1;
    color: var(--text-light);
  }
  .owner-name {
    position: absolute;
    left: 0;
    top: 480px;
    width: 1200px;
    margin: 0;
    text-align: center;
    font-family: "Yellowtail", "Brush Script MT", cursive;
    font-weight: 400;
    font-size: 42px;
    line-height: 1;
    color: var(--accent-red);
  }
  .contact-list {
    position: absolute;
    left: 48px;
    top: 44px;
    margin: 0;
    padding: 0;
    list-style: none;
    font-family: "Montserrat", sans-serif;
    font-weight: 400;
    font-size: 16px;
    line-height: 26px;
    color: var(--text-soft);
  }
  .contact-list .contact-web {
    color: var(--text-light);
  }
</style>
</head>
<body>
  <main class="card">
    <svg class="berry-wave" viewBox="0 0 1200 777" role="img" aria-label="Decorative wave of scattered wine-coloured berries and small green leaves">
      <defs>
        <linearGradient id="berryTone" x1="0" y1="0" x2="1" y2="1">
          <stop offset="0" stop-color="#6e3a4a" stop-opacity="0.75"/>
          <stop offset="0.5" stop-color="#8a2a33" stop-opacity="0.85"/>
          <stop offset="1" stop-color="#5a1a24" stop-opacity="0.9"/>
        </linearGradient>
      </defs>
      <path d="M0,470 C140,500 240,690 430,700 C620,705 780,610 900,470 C950,400 980,330 1010,330 L1200,330 L1200,777 L0,777 Z" fill="url(#berryTone)"/>
    </svg>

    <ul class="contact-list">
      <li class="contact-web">www.theottertyeamug.example</li>
      <li>facebook.com/theottertyeamug</li>
      <li>twitter.com/otter_brew</li>
      <li>instagram.com/theottertyeamug</li>
    </ul>

    <p class="brand-mark">The Otter Tea Mug</p>

    <svg class="glass-art" viewBox="0 0 77 167" role="img" aria-label="Wine glass illustration with brand symbol inside">
      <rect width="77" height="167" rx="6" fill="#4a2a2c"/>
    </svg>

    <h1 class="wordmark">TheOtterTeaMug</h1>
    <p class="owner-name">Dorian Fenwick</p>
  </main>
</body>
</html>
```